Property development business card design

New build residential property developers. I want a professional look but customer friendly so not too corporate. I'm not sure what logo will look best so open to designs with either. Thank you

Also i don't want both names on one card its 2 names for 2 different cards but with the same design.

Industry/Entity Type

Residential

Contact Information for Business Card

TRW Developments Ltd,
58 Fennick Lane,
Ipswich,
Suffolk,
IP7 2DX

Property Research Manager
Judith Penrow

Managing Director
Dermot Aldwick

```html
<!DOCTYPE html>
<html lang="en">
<head>
<meta charset="utf-8">
<title>TRW Developments – Business Card</title>
<link rel="stylesheet" href="https://fonts.googleapis.com/css2?family=Exo+2:wght@400;600&display=swap">
<style>
  :root {
    --page-bg: #e6e8eb;
    --card-white: #ffffff;
    --blue-deep: #2f3f9e;
    --blue-mid: #2f6fce;
    --blue-light: #1aa0e4;
    --swoosh-dark: #3a3d42;
    --swoosh-light: #b9bcc1;
    --text-grey: #8a8d92;
    --text-dark: #2b2d30;
  }
  * { box-sizing: border-box; margin: 0; padding: 0; }
  html, body {
    width: 1200px; height: 901px; overflow: hidden;
    background: var(--page-bg);
    font-family: "Exo 2", sans-serif;
  }
  .business-card {
    position: absolute; left: 150px; top: 190px;
    width: 900px; height: 520px;
    border-radius: 44px; overflow: hidden;
    background: var(--card-white);
    box-shadow: 0 14px 40px rgba(0,0,0,.18);
  }
  .card-art { position: absolute; inset: 0; }
  .brand {
    position: absolute; left: 48px; top: 78px;
    display: flex; align-items: center; gap: 16px;
  }
  .brand-mark {
    width: 88px; height: 88px; border-radius: 50%;
    background: var(--blue-mid);
    border: 6px solid #d7dadd;
    flex: none;
  }
  .brand-name {
    font-weight: 600; font-size: 20px; letter-spacing: 1px;
    color: var(--text-grey); text-transform: uppercase;
    margin-top: 34px; white-space: nowrap;
  }
  .person {
    position: absolute; right: 46px; top: 104px;
    text-align: right; color: #fff;
  }
  .person-name { font-weight: 600; font-size: 26px; letter-spacing: 1.5px; }
  .person-role { font-weight: 400; font-size: 19px; margin-top: 2px; }
  .contact-list {
    position: absolute; left: 40px; top: 238px;
    list-style: none; color: var(--text-dark);
    font-size: 17px; letter-spacing: 1.2px;
  }
  .contact-list li { display: flex; align-items: center; gap: 12px; height: 26px; }
  .contact-list svg { width: 18px; height: 18px; fill: var(--blue-mid); flex: none; }
  .address {
    position: absolute; right: 262px; bottom: 42px;
    text-align: right; color: var(--text-dark);
    font-size: 20px; letter-spacing: 1.2px; line-height: 1.35;
  }
</style>
</head>
<body>
  <div class="business-card">
    <svg class="card-art" viewBox="0 0 900 520" preserveAspectRatio="none" aria-hidden="true">
      <defs>
        <linearGradient id="blueField" x1="0" y1="0" x2="1" y2="0">
          <stop offset="0" stop-color="var(--blue-deep)"/>
          <stop offset="0.5" stop-color="var(--blue-mid)"/>
          <stop offset="1" stop-color="var(--blue-light)"/>
        </linearGradient>
        <linearGradient id="swoosh" x1="0" y1="0" x2="1" y2="1">
          <stop offset="0" stop-color="var(--swoosh-light)"/>
          <stop offset="0.6" stop-color="var(--swoosh-dark)"/>
          <stop offset="1" stop-color="var(--swoosh-dark)"/>
        </linearGradient>
      </defs>
      <path d="M0,0 H900 V520 H740 C700,280 530,40 0,32 Z" fill="url(#blueField)"/>
      <path d="M0,44 C520,52 690,290 720,520 H740 C700,280 530,40 0,32 Z" fill="#ffffff"/>
      <path d="M0,50 C515,60 680,295 704,520 H720 C690,290 520,52 0,44 Z" fill="url(#swoosh)"/>
    </svg>

    <div class="brand">
      <div class="brand-mark"></div>
      <div class="brand-name">TRW Developments</div>
    </div>

    <div class="person">
      <div class="person-name">DERMOT ALDWICK</div>
      <div class="person-role">Managing Director</div>
    </div>

    <ul class="contact-list">
      <li><svg viewBox="0 0 24 24"><path d="M6.6 10.8a15 15 0 0 0 6.6 6.6l2.2-2.2c.3-.3.7-.4 1-.2 1.1.4 2.3.6 3.6.6.6 0 1 .4 1 1V20c0 .6-.4 1-1 1A17 17 0 0 1 3 4c0-.6.4-1 1-1h3.5c.6 0 1 .4 1 1 0 1.3.2 2.5.6 3.6.1.3 0 .7-.2 1z"/></svg>01473 555 018</li>
      <li><svg viewBox="0 0 24 24"><path d="M7 1h10a2 2 0 0 1 2 2v18a2 2 0 0 1-2 2H7a2 2 0 0 1-2-2V3a2 2 0 0 1 2-2zm0 3v14h10V4z"/></svg>01473 555 019</li>
      <li><svg viewBox="0 0 24 24"><path d="M3 8h4v13H3zM9 3h12v18H9zm3 3v3h6V6zm0 5v2h2v-2zm4 0v2h2v-2zm-4 4v2h2v-2zm4 0v2h2v-2z"/></svg>01473 555 020</li>
      <li><svg viewBox="0 0 24 24"><path d="M2 5h20v14H2zm2 2v.5l8 5 8-5V7z"/></svg>dermot@trwdev.co.uk</li>
      <li><svg viewBox="0 0 24 24"><path d="M12 2a10 10 0 1 0 0 20 10 10 0 0 0 0-20zm6.9 9h-3a15 15 0 0 0-1.3-5.6A8 8 0 0 1 18.9 11zM12 4c.9 1.3 1.7 3.7 1.9 7h-3.8c.2-3.3 1-5.7 1.9-7zM9.4 5.4A15 15 0 0 0 8.1 11h-3a8 8 0 0 1 4.3-5.6zM5.1 13h3a15 15 0 0 0 1.3 5.6A8 8 0 0 1 5.1 13zM12 20c-.9-1.3-1.7-3.7-1.9-7h3.8c-.2 3.3-1 5.7-1.9 7zm2.6-1.4a15 15 0 0 0 1.3-5.6h3a8 8 0 0 1-4.3 5.6z"/></svg>www.trwdev.co.uk</li>
    </ul>

    <div class="address">
      58 Fennick Lane,<br>
      Ipswich IP7 2DX
    </div>
  </div>
</body>
</html>
```